Past the Gravel

I need a book cover designed - 6 inches wide x 9 inches tall. I would like it Past the predominantly black and white, with a big bold title as attached:
Past the
GRAVEL
I have attached a black and white photo that I would like to cover the bottom half (or close to it) of the book, with the words: Life Lessons That Helped Build QTR, Pike B Dam, And Transform Loviter & BLUZ TV
By Gavin Melrose
The designs I've included here I don't particularly like, although I think you can see my general idea. He is a black and white man, so I have a back and white photo.
A big bold headline and not overly sized black and white

```html
<!DOCTYPE html>
<html lang="en">
<head>
<meta charset="utf-8">
<title>Past the Gravel — Book Cover</title>
<link rel="stylesheet" href="https://fonts.googleapis.com/css2?family=Poppins:ital,wght@0,500;1,400&family=Roboto+Slab:wght@100..900&display=swap">
<style>
  :root {
    --page: #ffffff;
    --cover: #050505;
    --ink: #fdf6f6;
    --photo-light: #5a5a5a;
    --photo-mid: #2a2a2a;
  }
  html, body {
    margin: 0;
    width: 1200px;
    height: 1200px;
    overflow: hidden;
    background: var(--page);
  }
  .canvas {
    position: relative;
    width: 1200px;
    height: 1200px;
  }
  .book-cover {
    position: absolute;
    left: 228px;
    top: 56px;
    width: 724px;
    height: 1087px;
    display: block;
  }
  .title-top {
    font-family: "Poppins", sans-serif;
    font-weight: 500;
    font-size: 112px;
    fill: var(--ink);
  }
  .title-main {
    font-family: "Roboto Slab", serif;
    font-weight: 900;
    font-size: 172px;
    fill: var(--ink);
  }
  .subtitle {
    font-family: "Poppins", sans-serif;
    font-style: italic;
    font-weight: 400;
    font-size: 25px;
    letter-spacing: 0.5px;
    fill: var(--ink);
  }
  .author {
    font-family: "Roboto Slab", serif;
    font-weight: 700;
    font-size: 25px;
    fill: var(--ink);
  }
  .ink-fill { fill: var(--ink); }
  .ink-stroke { stroke: var(--ink); }
</style>
</head>
<body>
<div class="canvas">
  <svg class="book-cover" viewBox="0 0 724 1087" xmlns="http://www.w3.org/2000/svg">
    <defs>
      <radialGradient id="portraitGlow" cx="0.6" cy="0.35" r="0.6">
        <stop offset="0" stop-color="#5a5a5a"/>
        <stop offset="0.45" stop-color="#2a2a2a"/>
        <stop offset="1" stop-color="#050505"/>
      </radialGradient>
    </defs>

    <rect class="cover-background" width="724" height="1087" fill="var(--cover)"/>

    <rect class="author-portrait" role="img" aria-label="Black and white portrait photograph of the author against a dark smoky background"
          x="300" y="330" width="424" height="520" fill="url(#portraitGlow)"/>

    <g class="title-dots title-dots--left ink-fill">
      <circle cx="55" cy="102" r="3.7"/><circle cx="71.5" cy="102" r="3.7"/><circle cx="88" cy="102" r="3.7"/>
      <circle cx="104.5" cy="102" r="3.7"/><circle cx="121" cy="102" r="3.7"/><circle cx="137.5" cy="102" r="3.7"/>
    </g>
    <text class="title-top" x="158" y="137" textLength="408" lengthAdjust="spacingAndGlyphs">Past the</text>
    <g class="title-dots title-dots--right ink-fill">
      <circle cx="586.5" cy="102" r="3.7"/><circle cx="603" cy="102" r="3.7"/><circle cx="619.5" cy="102" r="3.7"/>
      <circle cx="636" cy="102" r="3.7"/><circle cx="652.5" cy="102" r="3.7"/><circle cx="669" cy="102" r="3.7"/>
    </g>

    <text class="title-main" x="50" y="291" textLength="632" lengthAdjust="spacingAndGlyphs">GRAVEL</text>

    <text class="subtitle" text-anchor="middle">
      <tspan x="192" y="552">LIFE LESSONS THAT</tspan>
      <tspan x="192" y="582">HELPED BUILD QTR,</tspan>
      <tspan x="192" y="612">PIKE B DAM,</tspan>
      <tspan x="192" y="642">AND TRANSFORM</tspan>
      <tspan x="192" y="672">LOVITER &amp; BLUZ TV</tspan>
    </text>

    <g class="subtitle-dots ink-fill">
      <circle cx="59" cy="765" r="3.7"/><circle cx="75.5" cy="765" r="3.7"/><circle cx="92" cy="765" r="3.7"/>
      <circle cx="108.5" cy="765" r="3.7"/><circle cx="125" cy="765" r="3.7"/><circle cx="141.5" cy="765" r="3.7"/>
      <circle cx="158" cy="765" r="3.7"/><circle cx="174.5" cy="765" r="3.7"/><circle cx="191" cy="765" r="3.7"/>
      <circle cx="207.5" cy="765" r="3.7"/><circle cx="224" cy="765" r="3.7"/><circle cx="240.5" cy="765" r="3.7"/>
      <circle cx="257" cy="765" r="3.7"/><circle cx="273.5" cy="765" r="3.7"/><circle cx="290" cy="765" r="3.7"/>
      <circle cx="306.5" cy="765" r="3.7"/><circle cx="323" cy="765" r="3.7"/>
    </g>

    <text class="author" x="80" y="939">By Gavin Melrose</text>
    <line class="author-rule ink-stroke" x1="318" y1="929" x2="682" y2="929" stroke-width="4"/>
  </svg>
</div>
</body>
</html>
```